Nightclub-type Event Poster Advertisement

Lumora Events is based in Christchurch, New Zealand and we have our next party coming up. We like a different flair for each of our events so are looking for some help from you guys. We are very flexible with everything - colours, layout, backgrounds, fonts, etc so it's ALL up to you. Attached is our company logo and the flyer (and poster) we used for our last party. Our website is lumoranz.example where you can find and use our photos and find more info about us if you desire.
Designs we are wanting: An A3 poster,an A6 flyer (smaller version of the poster is probably fine), tickets (140x68 mm). It would be great if a 5 mm bleed was included so we could get them printed directly.
Details for the event to be advertised are as followed:
Party Name: (TBD... will update ASAP)
05/07/2014
10pm-close
Lineup: 'Bazzo (Akl)', 'DJ Glimtrax', 'DJ's Morquent & Pelnavo', 'Quiet Harbour Pulse'.
Dorrin Hattles Central, Corner Fenwick & Oberly Streets
$10 Tickets
R18
Tickets & Enquiries: Marta on 0219047362
Presented by Lumora Entertainment
Thanks to everyone who reads this and please give it a go! Any questions don't hesitate to ask.
Target Market(s)
New Zealand Europeans in Christchurch, New Zealand between 18 and 25 years old.
Industry/Entity Type
Events
Look and feel

```html
<!DOCTYPE html>
<html lang="en">
<head>
<meta charset="utf-8">
<title>Lumora Events – 05/07/2014</title>
<link rel="stylesheet" href="https://fonts.googleapis.com/css2?family=Orbitron:wght@500;700;900&family=Russo+One&display=swap">
<style>
  :root {
    --teal: #2fc4b0;
    --teal-deep: #1a8f86;
    --pink: #f35a7a;
    --coral: #f7866f;
    --ink: #000000;
    --white: #ffffff;
  }
  html, body {
    margin: 0;
    padding: 0;
    width: 849px;
    height: 1200px;
    overflow: hidden;
    background: var(--white);
  }
  .poster {
    position: relative;
    width: 849px;
    height: 1200px;
    overflow: hidden;
  }
  .poster svg { display: block; }
  .date { font-family: "Orbitron", sans-serif; font-weight: 700; font-size: 43px; fill: var(--white); letter-spacing: 3px; }
  .event-title { font-family: "Orbitron", sans-serif; font-weight: 900; font-size: 80px; letter-spacing: 5px; }
  .lineup { font-family: "Orbitron", sans-serif; font-weight: 700; font-size: 27px; fill: var(--white); letter-spacing: 1px; }
  .brand-mark { font-family: "Orbitron", sans-serif; font-weight: 700; font-size: 15px; fill: var(--teal); letter-spacing: 2px; }
  .brand-corner { font-family: "Orbitron", sans-serif; font-weight: 700; font-size: 22px; fill: var(--ink); letter-spacing: 1px; }
  .info { font-family: "Orbitron", sans-serif; font-weight: 500; font-size: 40px; fill: none; stroke: var(--ink); stroke-width: 1.2px; }
  .info-strong { font-family: "Orbitron", sans-serif; font-weight: 900; fill: var(--ink); stroke: none; }
  .venue { font-family: "Russo One", sans-serif; font-size: 25px; fill: var(--white); letter-spacing: 1px; }
  .presented { font-family: "Russo One", sans-serif; font-size: 25px; fill: var(--white); letter-spacing: 1.5px; }
  .enquiries { font-family: "Russo One", sans-serif; font-size: 25px; fill: var(--ink); letter-spacing: 1.5px; }
  .enquiries-name { fill: none; stroke: var(--ink); stroke-width: 0.9px; }
  .bolt { fill: none; stroke: var(--ink); stroke-width: 15; stroke-linejoin: miter; stroke-miterlimit: 12; stroke-linecap: butt; }
</style>
</head>
<body>
<main class="poster">
  <svg width="849" height="1200" viewBox="0 0 849 1200" xmlns="http://www.w3.org/2000/svg">
    <defs>
      <linearGradient id="sky" x1="0" y1="0" x2="0" y2="1">
        <stop offset="0" stop-color="#2cb8a6"/>
        <stop offset="0.3" stop-color="#3fb9a2"/>
        <stop offset="0.48" stop-color="#b98b8c"/>
        <stop offset="0.62" stop-color="#f25e7c"/>
        <stop offset="1" stop-color="#f7806f"/>
      </linearGradient>
      <linearGradient id="ring" x1="0" y1="0" x2="0" y2="1">
        <stop offset="0" stop-color="var(--teal)"/>
        <stop offset="1" stop-color="var(--pink)"/>
      </linearGradient>
      <linearGradient id="title-fill" x1="0" y1="0" x2="1" y2="0">
        <stop offset="0" stop-color="#8a9a9c"/>
        <stop offset="0.5" stop-color="var(--teal)"/>
        <stop offset="1" stop-color="#c9a2a8"/>
      </linearGradient>
    </defs>

    <rect class="backdrop" role="img" aria-label="Starry teal nebula sky blending into a pink and coral cloudy glow" x="0" y="0" width="849" height="1200" fill="url(#sky)"/>

    <text class="date" x="428" y="94" text-anchor="middle">05/07/2014</text>

    <g class="headline-disc">
      <circle cx="422" cy="478" r="340" fill="none" stroke="url(#ring)" stroke-width="4"/>
      <circle cx="422" cy="478" r="330" fill="var(--ink)"/>
    </g>

    <g class="disc-brand">
      <rect x="346" y="302" width="10" height="10" fill="var(--teal)"/>
      <text class="brand-mark" x="364" y="313">LUMORA EVENTS</text>
    </g>

    <text class="event-title" x="414" y="492" text-anchor="middle" fill="url(#title-fill)">TITLE HERE</text>

    <g class="lineup-list" text-anchor="middle">
      <text class="lineup" x="422" y="594">BAZZO (AKL)</text>
      <text class="lineup" x="422" y="634">DJ GLIMTRAX</text>
      <text class="lineup" x="422" y="674">DJ'S MORQUENT &amp; PELNAVO</text>
      <text class="lineup" x="422" y="714">QUIET HARBOUR PULSE</text>
    </g>

    <polyline class="bolt" points="418,808 362,886 438,904 366,972 420,986 372,1046"/>

    <g class="entry-details">
      <text class="info" x="68" y="892">R18</text>
      <text class="info" x="68" y="947"><tspan class="info-strong">$10</tspan> Tickets</text>
      <text class="info" x="68" y="1002">10 pm <tspan class="info-strong">close</tspan></text>
    </g>

    <g class="venue-block" text-anchor="middle">
      <text class="venue" x="627" y="872">Dorrin Hattles Central</text>
      <text class="venue" x="627" y="908">Corner Fenwick &amp;</text>
      <text class="venue" x="627" y="944">Oberly Streets</text>
    </g>

    <g class="corner-brand">
      <rect x="620" y="1042" width="14" height="14" fill="var(--ink)"/>
      <text class="brand-corner" x="642" y="1057">LUMORA</text>
      <text class="brand-corner" x="642" y="1085">EVENTS</text>
    </g>

    <text class="presented" x="68" y="1108">Presented by Lumora Entertainment</text>
    <text class="enquiries" x="68" y="1152">Tickets &amp; Enquiries: <tspan class="enquiries-name">Marta on</tspan> 0219047362</text>
  </svg>
</main>
</body>
</html>
```